Natural Medicine & Health/Fitness Coaching studio requires web page

Require a innovative web page for a studio that coaches clients to better health, nutrition and fitness. The studio compromises of Clinical Nutritionists, Naturopaths, Rehab Trainers, Personal Trainers and Sport Coaches. Would like to see earthy but bold designs emphasizing nutritional health and athletic performance.
Updates

Design only launched today.

Target Market(s)

All genders from 20's to 60's, as well as families

Industry/Entity Type

Nutritionist

Coding

Coded - Design and coding required

Number of Pages Required

3 page

Colors
abd037
3277b5
fbee3d
fece3e
33b8a4
f04a50

Requirements
Must have
• Online booking system, ability to message
• Home page
• Coaching/Fitness page
• Nutritional Medicine page
• Must be suitable for both Fitness and Nutrition

```html
<!DOCTYPE html>
<html lang="en">
<head>
<meta charset="utf-8">
<title>Summit Fit – Nutritional Therapy</title>
<link href="https://fonts.googleapis.com/css2?family=Lato:ital,wght@0,400;0,700;0,900;1,700&family=Raleway:ital,wght@0,400;0,500;0,600;0,700;1,700&family=Merriweather:wght@700&display=swap" rel="stylesheet">
<style>
:root{
  --green:#8cc43f;
  --green-dark:#78ad2e;
  --ink:#2b2b2b;
  --text:#555;
  --muted:#888;
  --white:#fff;
  --light:#f2f2f2;
  --line:#d9d9d9;
  --blue:#1e5d8c;
  --navy:#173b57;
  --black:#0c0c0c;
  --footer-base:#2f2f2f;
}
*{margin:0;padding:0;box-sizing:border-box}
html,body{width:1200px;height:4489px;overflow:hidden}
body{font-family:'Lato',sans-serif;color:var(--text);background:var(--white);position:relative}
.section{position:absolute;left:0;width:1200px;overflow:hidden}
.abs{position:absolute}
.btn{position:absolute;display:flex;align-items:center;justify-content:center;background:var(--green);color:var(--white);border-radius:22px;font:700 15px 'Lato',sans-serif}
.title{position:absolute;left:0;width:1200px;text-align:center;font:500 28px 'Raleway',sans-serif;color:var(--ink)}
.lead{position:absolute;left:240px;width:720px;text-align:center;font-size:13px;line-height:20px;color:var(--text)}

/* header */
.header{top:0;height:96px;background:var(--white)}
.brand{left:120px;top:18px;display:flex;align-items:center;gap:8px}
.brand-mark{width:14px;height:14px;background:var(--green);border-radius:50%}
.brand-name{font:700 30px 'Lato',sans-serif;color:var(--green)}
.brand-sub{position:absolute;left:142px;top:60px;font-size:10px;color:var(--muted);letter-spacing:1px}
.nav{right:110px;top:38px;display:flex;gap:30px;font:600 15px 'Raleway',sans-serif;color:var(--ink)}
.nav .active{color:var(--green);border-bottom:3px solid var(--green);padding-bottom:6px}

/* hero */
.hero{top:96px;height:544px;background:linear-gradient(100deg,#111 0%,#2c2c2c 40%,#4a4a4a 60%,#1b1b1b 100%)}
.hero-kicker{left:120px;top:178px;font:700 31px 'Merriweather',serif;color:var(--white)}
.hero-title{left:120px;top:214px;font:700 52px 'Raleway',sans-serif;color:var(--white)}
.hero-text{left:120px;top:284px;width:420px;font-size:15px;line-height:21px;color:var(--white)}

/* why */
.why{top:640px;height:476px;background:var(--white)}
.why-card{position:absolute;top:182px;width:292px;height:219px}
.why-photo{height:178px;width:100%}
.why-label{height:41px;background:var(--green);color:var(--white);font:600 14px 'Raleway',sans-serif;display:flex;align-items:center;justify-content:center}

/* services */
.services{top:1116px;height:654px;background:var(--light)}
.service{position:absolute;width:297px;height:165px;background:var(--white);padding:18px 22px}
.service-head{display:flex;align-items:center;gap:12px;font:600 18px 'Raleway',sans-serif;color:var(--ink)}
.icon{width:34px;height:34px;border-radius:50%;background:var(--green);display:flex;align-items:center;justify-content:center;flex:none}
.service p{margin-top:12px;font-size:13px;line-height:19px;color:var(--text)}
.more{font-size:12px;color:var(--green);font-weight:700}

/* course banner */
.course{top:1770px;height:330px;background:linear-gradient(90deg,#1f3a1f 0%,#3f6a2b 45%,#7fa049 70%,#3c5a26 100%)}
.course-title{left:120px;top:78px;font:italic 700 26px 'Raleway',sans-serif;color:var(--white)}
.course-text{left:120px;top:124px;width:300px;font-size:13px;line-height:18px;color:var(--white)}

/* coaches */
.coaches{top:2100px;height:540px;background:var(--white)}
.coach{position:absolute;top:162px;width:216px;height:279px}
.coach-photo{height:216px}
.coach-label{height:63px;background:var(--green);color:var(--white);text-align:center;padding-top:13px}
.coach-label b{display:block;font:700 14px 'Raleway',sans-serif}
.coach-label span{font-size:12px}

/* offer */
.offer{top:2640px;height:330px;background:linear-gradient(90deg,#101010 0%,#2a2a2a 40%,#3a3632 60%,#1a1a1a 100%)}
.offer-title{left:606px;top:78px;font:italic 700 29px 'Raleway',sans-serif;color:var(--white)}
.offer-text{left:606px;top:122px;font:400 24px 'Raleway',sans-serif;line-height:30px;color:var(--white)}

/* testimonials */
.testimonials{top:2970px;height:396px;background:var(--white)}
.avatar{position:absolute;width:75px;height:75px;border-radius:50%}
.quote{position:absolute;width:327px;height:138px;border:1px solid var(--line);padding:14px 18px;font-size:13px;line-height:19px;color:var(--text)}
.quote::before{content:"";position:absolute;left:-9px;top:24px;width:16px;height:16px;background:var(--white);border-left:1px solid var(--line);border-bottom:1px solid var(--line);transform:rotate(45deg)}
.quote .who{margin-top:10px;color:var(--green);font-weight:700}
.quote .note{font-size:11px;color:var(--muted);line-height:14px}

/* stats */
.stats{top:3366px;height:288px;background:linear-gradient(180deg,#0d2336 0%,#1d3b55 50%,#0f273b 100%)}
.stat{position:absolute;top:64px;width:220px;text-align:center;color:var(--white)}
.stat b{display:block;font:700 60px 'Lato',sans-serif}
.stat i{display:block;width:40px;height:3px;background:var(--white);margin:6px auto 18px}
.stat span{font-size:13px;line-height:18px}

/* contact */
.contact{top:3654px;height:360px;background:var(--white)}
.field{position:absolute;height:36px;border:1px solid #bbb;border-radius:4px;padding:9px 12px;font-size:13px;color:var(--text)}
.field sup{color:#d33}
.submit{position:absolute;left:165px;top:276px;width:150px;height:45px;border:1px solid #999;border-radius:23px;font:700 15px 'Lato',sans-serif;color:var(--ink);display:flex;align-items:center;justify-content:center}
.contact-photo{left:675px;top:0;width:525px;height:360px;background:linear-gradient(135deg,#9aa08f 0%,#c9b8a2 45%,#7a6a5c 100%)}
.request{left:690px;top:144px;width:459px;height:150px;background:rgba(140,196,63,.92);padding:20px 30px;color:var(--white)}
.request em{font:italic 700 20px 'Raleway',sans-serif;display:block}
.request strong{font:500 24px 'Raleway',sans-serif;display:block}
.request p{font-size:12px;line-height:17px;margin-top:6px}

/* newsletter */
.newsletter{top:4014px;height:72px;background:var(--blue)}
.nl-icon{left:162px;top:18px;width:36px;height:36px;border-radius:50%;background:var(--white);display:flex;align-items:center;justify-content:center}
.nl-title{left:219px;top:22px;font:400 23px 'Raleway',sans-serif;color:var(--white)}
.nl-input{left:498px;top:21px;width:396px;height:30px;background:var(--white);font-size:12px;padding:8px 10px;color:var(--muted)}
.nl-btn{left:909px;top:21px;width:132px;height:30px;background:var(--navy);color:var(--white);font:700 12px 'Lato',sans-serif;display:flex;align-items:center;justify-content:center}

/* footer */
.footer{top:4086px;height:342px;background:var(--black);color:var(--white)}
.f-brand{left:126px;top:96px;display:flex;align-items:center;gap:8px;font:900 20px 'Lato',sans-serif}
.f-brand i{width:12px;height:12px;background:var(--white)}
.f-follow{left:126px;top:168px;font-size:15px}
.socials{left:126px;top:194px;display:flex;gap:6px}
.socials i{width:22px;height:22px;border:1.5px solid var(--white);border-radius:50%}
.f-head{top:90px;font:500 16px 'Raleway',sans-serif;letter-spacing:.5px}
.f-list{font-size:13px;line-height:22px}
.f-row{display:flex;gap:14px;align-items:flex-start;font-size:13px;line-height:18px;margin-bottom:14px}
.f-input{position:absolute;height:36px;background:var(--white);color:var(--muted);font-size:12px;padding:10px}
.f-send{left:819px;top:267px;width:132px;height:39px;background:var(--green);display:flex;align-items:center;justify-content:center;font:700 14px 'Lato',sans-serif}
.copyright{top:4428px;height:61px;background:var(--footer-base);color:#aaa;font-size:12px;display:flex;align-items:center;justify-content:center}
</style>
</head>
<body>

<header class="section header">
  <div class="abs brand"><span class="brand-name">Summit Fit</span><span class="brand-mark"></span></div>
  <div class="brand-sub">Nutritional Therapy</div>
  <nav class="abs nav">
    <span class="active">Home</span><span>Fitness ▾</span><span>Nutrition ▾</span><span>Coaching ▾</span><span>Contact Us ▾</span>
  </nav>
</header>

<section class="section hero" role="img" aria-label="Photo of a woman training on a stability ball in a dark gym">
  <div class="abs hero-kicker">Acheive your fitness goal with our</div>
  <div class="abs hero-title">amazing personal trainer</div>
  <p class="abs hero-text">Summit-Fit-Nutritional-Therapy coaches clients to better health, nutrition and fitness. We specialize in Nutritional health &amp; athletic performance.</p>
  <div class="btn" style="left:120px;top:378px;width:156px;height:42px">Learn Now</div>
</section>

<section class="section why">
  <h2 class="title" style="top:68px">Why Us</h2>
  <p class="lead" style="top:110px">Summit-Fit-Nutritional-Therapy coaches clients to better health, nutrition and fitness. The studio compromises of Clinical Nutritionists, Naturopaths, Rehab Trainers, Personal Trainers and Sport Coaches. We specialize in Nutritional health &amp; athletic performance.</p>
  <div class="why-card" style="left:132px"><div class="why-photo" role="img" aria-label="Photo of fresh fruit and vegetables beside a diet plan" style="background:linear-gradient(135deg,#d9a441,#8fb54a,#c64a3a)"></div><div class="why-label">Customized Workout &amp; Diet Plan</div></div>
  <div class="why-card" style="left:454px"><div class="why-photo" role="img" aria-label="Photo of smiling women in a coaching session" style="background:linear-gradient(135deg,#c9a58a,#7c5a48,#d8c0ad)"></div><div class="why-label">Personal Coaching</div></div>
  <div class="why-card" style="left:776px"><div class="why-photo" role="img" aria-label="Photo of people exercising together in a gym" style="background:linear-gradient(135deg,#3b3b3b,#8a7a6a,#2a2a2a)"></div><div class="why-label">Motivation &amp; Support</div></div>
</section>

<section class="section services">
  <h2 class="title" style="top:72px">Our Services</h2>
  <p class="lead" style="top:114px">Summit-Fit-Nutritional-Therapy coaches clients to better health, nutrition and fitness. The studio compromises of Clinical Nutritionists, Naturopaths, Rehab Trainers, Personal Trainers and Sport Coaches. We specialize in Nutritional health &amp; athletic performance.</p>

  <div class="service" style="left:132px;top:207px"><div class="service-head"><span class="icon"><svg width="16" height="16" viewBox="0 0 16 16"><path d="M3 13 C3 6 8 3 13 3 C13 9 9 13 3 13Z" fill="#fff"/></svg></span>Nutrition</div><p>Lorem ipsum dolor sit amet, consectetur adipiscing elit. Quid autem habent admira-tionis, cum prope accessris.<br><span class="more">Read More →</span></p></div>
  <div class="service" style="left:452px;top:207px"><div class="service-head"><span class="icon"><svg width="18" height="12" viewBox="0 0 18 12"><rect x="0" y="3" width="3" height="6" fill="#fff"/><rect x="15" y="3" width="3" height="6" fill="#fff"/><rect x="3" y="5" width="12" height="2" fill="#fff"/></svg></span>Fitness</div><p>Lorem ipsum dolor sit amet, consectetur adipiscing elit. Quid autem habent admira-tionis, cum prope accessris.<br><span class="more">Read More →</span></p></div>
  <div class="service" style="left:772px;top:207px"><div class="service-head"><span class="icon"><svg width="16" height="16" viewBox="0 0 16 16"><path d="M2 12 L6 7 L9 10 L14 4" stroke="#fff" stroke-width="2" fill="none"/></svg></span>Performance</div><p>Lorem ipsum dolor sit amet, consectetur adipiscing elit. Quid autem habent admira-tionis, cum prope accessris.<br><span class="more">Read More →</span></p></div>

  <div class="service" style="left:132px;top:399px"><div class="service-head"><span class="icon"><svg width="16" height="16" viewBox="0 0 16 16"><circle cx="8" cy="8" r="6" stroke="#fff" stroke-width="2" fill="none"/><path d="M8 8 L11 5" stroke="#fff" stroke-width="2"/></svg></span>Weight Loss</div><p>Lorem ipsum dolor sit amet, consectetur adipiscing elit. Quid autem habent admira-tionis, cum prope accessris.<br><span class="more">Read More →</span></p></div>
  <div class="service" style="left:452px;top:399px"><div class="service-head"><span class="icon"><svg width="16" height="16" viewBox="0 0 16 16"><path d="M8 14 L2 8 A3 3 0 0 1 8 4 A3 3 0 0 1 14 8 Z" fill="#fff"/></svg></span>Cardio</div><p>Lorem ipsum dolor sit amet, consectetur adipiscing elit. Quid autem habent admira-tionis, cum prope accessris.<br><span class="more">Read More →</span></p></div>
  <div class="service" style="left:772px;top:399px"><div class="service-head"><span class="icon"><svg width="16" height="16" viewBox="0 0 16 16"><path d="M5 3 L13 8 L5 13 Z" fill="#fff"/></svg></span>Viedo Lession</div><p>Lorem ipsum dolor sit amet, consectetur adipiscing elit. Quid autem habent admira-tionis, cum prope accessris.<br><span class="more">Read More →</span></p></div>
</section>

<section class="section course" role="img" aria-label="Photo of a man and a woman jogging outdoors among green trees">
  <div class="abs course-title">3 months Better you Course</div>
  <p class="abs course-text">Start working on your fitness &amp; Nutrition with our personal trainer, and see a better you in 3 months</p>
  <div class="btn" style="left:120px;top:204px;width:180px;height:42px">Get Appointment</div>
</section>

<section class="section coaches">
  <h2 class="title" style="top:84px">Our Coaches</h2>
  <div class="coach" style="left:132px"><div class="coach-photo" role="img" aria-label="Photo of a bodybuilding coach" style="background:linear-gradient(135deg,#5a4a3e,#a58a74)"></div><div class="coach-label"><b>MARCO VELLANI</b><span>Bodybuilding</span></div></div>
  <div class="coach" style="left:372px"><div class="coach-photo" role="img" aria-label="Photo of a fitness coach" style="background:linear-gradient(135deg,#c7b8aa,#6f93a8)"></div><div class="coach-label"><b>CLARA WHITMORE</b><span>Fitness</span></div></div>
  <div class="coach" style="left:615px"><div class="coach-photo" role="img" aria-label="Photo of a nutrition coach with a salad" style="background:linear-gradient(135deg,#e7d9c9,#8fb35a)"></div><div class="coach-label"><b>NADIA FORDE</b><span>Nutrition</span></div></div>
  <div class="coach" style="left:855px"><div class="coach-photo" role="img" aria-label="Photo of a weight loss coach holding a clipboard" style="background:linear-gradient(135deg,#b98a5e,#c9432f)"></div><div class="coach-label"><b>THEO BALSAM</b><span>Weight Loss</span></div></div>
</section>

<section class="section offer" role="img" aria-label="Photo of dumbbells on a dark wooden floor">
  <div class="abs offer-title">Fitness Classes Are Running</div>
  <div class="abs offer-text">JOIN NOW AND<br>GET <b>50%</b> DISCOUNT</div>
  <div class="btn" style="left:606px;top:210px;width:186px;height:40px">Become A Member</div>
</section>

<section class="section testimonials">
  <h2 class="title" style="top:82px">What Our Clients Says</h2>
  <div class="avatar" role="img" aria-label="Client portrait" style="left:165px;top:171px;background:#b89a82"></div>
  <div class="quote" style="left:261px;top:168px">Lorem ipsum dolor sit amet, consectetur adipiscing elit. Quid autem habent admirationis, cum prope accessris? An hoc usque quaque
    <div class="who">- Sam Carter</div><div class="note">I lost 8 pounds in a week</div></div>
  <div class="avatar" role="img" aria-label="Client portrait" style="left:636px;top:171px;background:#d8c3b0"></div>
  <div class="quote" style="left:729px;top:168px">Lorem ipsum dolor sit amet, consectetur adipiscing elit. Quid autem habent admirationis, cum prope accessris? An hoc usque quaque
    <div class="who">- Lena Hart</div><div class="note">I lost 6 pounds in a week</div></div>
</section>

<section class="section stats" role="img" aria-label="Photo of a woman doing push-ups in a gym, tinted blue">
  <div class="stat" style="left:124px"><b>15</b><i></i><span>Years of coaching<br>Experience</span></div>
  <div class="stat" style="left:364px"><b>52</b><i></i><span>Content attended about<br>Fitness &amp; Nutrition</span></div>
  <div class="stat" style="left:604px"><b>542</b><i></i><span>Happy Customers in my<br>fitness class</span></div>
  <div class="stat" style="left:850px"><b>12</b><i></i><span>Weight Loss, Fitness &amp;<br>Nutrition Programmes</span></div>
</section>

<section class="section contact">
  <div class="field" style="left:165px;top:57px;width:186px">Name<sup>*</sup></div>
  <div class="field" style="left:378px;top:57px;width:186px">Phone<sup>*</sup></div>
  <div class="field" style="left:165px;top:105px;width:186px">Email<sup>*</sup></div>
  <div class="field" style="left:378px;top:105px;width:186px">Subject<sup>*</sup></div>
  <div class="field" style="left:165px;top:156px;width:399px;height:81px">Message<sup>*</sup></div>
  <div class="submit">Submit Now</div>
  <div class="abs contact-photo" role="img" aria-label="Photo of a smiling woman in a gym"></div>
  <div class="abs request"><em>Request</em><strong>Free Consulation</strong><p>It's free for you. Any Query Please Contact Us<br>And have your health</p></div>
</section>

<section class="section newsletter">
  <div class="abs nl-icon"><svg width="18" height="14" viewBox="0 0 18 14"><rect x="1" y="1" width="16" height="12" fill="none" stroke="#1e5d8c" stroke-width="1.6"/><path d="M1 1 L9 8 L17 1" fill="none" stroke="#1e5d8c" stroke-width="1.6"/></svg></div>
  <div class="abs nl-title">News letter Signup</div>
  <div class="abs nl-input">Enter Your Email</div>
  <div class="abs nl-btn">SUBSCRIBE</div>
</section>

<footer class="section footer">
  <div class="abs f-brand"><i></i>Core Motion Trainer</div>
  <div class="abs f-follow">FOLLOW US</div>
  <div class="abs socials"><i></i><i></i><i></i><i></i></div>

  <div class="abs f-head" style="left:366px">CONTACT US</div>
  <div class="abs" style="left:366px;top:132px">
    <div class="f-row"><svg width="12" height="16" viewBox="0 0 12 16"><path d="M6 15 C6 15 1 9 1 6 A5 5 0 0 1 11 6 C11 9 6 15 6 15Z" fill="#fff"/><circle cx="6" cy="6" r="2" fill="#0c0c0c"/></svg><span>418 Alder Grove Rd<br>Westbrook TX 75990</span></div>
    <div class="f-row"><svg width="12" height="14" viewBox="0 0 12 14"><path d="M2 1 L5 1 L6 4 L4 5 C5 8 6 9 8 10 L9 8 L12 9 L12 12 C7 13 1 7 2 1Z" fill="#fff"/></svg><span>555.0142.7788</span></div>
    <div class="f-row"><svg width="14" height="10" viewBox="0 0 14 10"><rect x="0" y="0" width="14" height="10" fill="#fff"/><path d="M0 0 L7 6 L14 0" stroke="#0c0c0c" fill="none"/></svg><span>hello@summitfit.com</span></div>
  </div>

  <div class="abs f-head" style="left:624px">ABOUT US</div>
  <div class="abs f-list" style="left:624px;top:128px">Home<br>Fitness<br>Nutrition<br>Coaching<br>Contact Us</div>

  <div class="abs f-head" style="left:819px">GET IN TOUCH</div>
  <div class="f-input" style="left:819px;top:132px;width:126px">Name</div>
  <div class="f-input" style="left:951px;top:132px;width:126px">Phone</div>
  <div class="f-input" style="left:819px;top:180px;width:258px">Email address</div>
  <div class="f-input" style="left:819px;top:222px;width:258px;height:36px"></div>
  <div class="abs f-send">SEND</div>
</footer>

<div class="section copyright">Copyright © 2017 summitfit – All Rights Reserved</div>

</body>
</html>
```